Need new look for home page of Makeup Artist Site

We want a new, clean, modern, professional look for the new design for our website. Our current site is at https://glowvra.com. We would like a high fashion site with diverse ethnic groups represented throughout the page. We like trelk.com as an example of style and user experience. This website is for people to look for a makeup artist or esthetician to come to their home and perform a service there. They will pay on the website and be able to review available service providers and choose one. We will need 2 additional pages once this design is approved. We will pay separately for those.

```html
<!DOCTYPE html>
<html lang="en">
<head>
<meta charset="utf-8">
<title>Glowvra — Professional Makeup at Home</title>
<link rel="stylesheet" href="https://fonts.googleapis.com/css2?family=Poppins:wght@300;400;500;600;700&display=swap">
<style>
  :root{
    --red:#d0021b;
    --red-dark:#a80016;
    --ink:#1d1d1d;
    --muted:#555;
    --blush:#f8ece7;
    --blush-deep:#efd9d1;
    --paper:#ffffff;
    --night:#000000;
    --foot:#f4f1f0;
    --line:#d9d9d9;
  }
  *{box-sizing:border-box;margin:0;padding:0}
  html,body{width:1200px;height:4432px;overflow:hidden}
  body{position:relative;background:var(--paper);font-family:'Poppins',sans-serif;color:var(--ink)}
  .abs{position:absolute}
  a{color:inherit;text-decoration:none}

  /* header */
  .site-header{left:0;top:0;width:1200px;height:112px;display:flex;align-items:center;justify-content:space-between;padding:0 60px}
  .nav{display:flex;gap:34px;font-size:17px;font-weight:500;align-items:center}
  .nav li{list-style:none;display:flex;align-items:center;gap:34px}
  .nav .dot{width:6px;height:6px;border-radius:50%;background:var(--red)}
  .brand{font-size:46px;font-weight:700;color:var(--red);letter-spacing:2px;text-transform:uppercase}
  .nav-apply{line-height:1.2;text-align:center}

  /* hero */
  .hero{left:0;top:112px;width:1200px;height:608px;background:var(--blush)}
  .hero h1{left:48px;top:100px;width:300px;font-size:44px;font-weight:600;line-height:1.2}
  .hero p{left:48px;top:232px;width:290px;font-size:15px;line-height:1.5;color:var(--muted)}
  .btn{display:inline-flex;align-items:center;justify-content:center;background:var(--red);color:#fff;font-size:13px;font-weight:500;text-transform:uppercase;height:44px;width:128px}
  .hero .btn{left:48px;top:392px}
  .hero-photo{top:68px;height:472px}
  .hero-photo.one{left:372px;width:380px;background:linear-gradient(160deg,#c9d3db,#8a96a2 55%,#2b2a30)}
  .hero-photo.two{left:760px;width:392px;background:linear-gradient(160deg,#2a2a2e,#6b5b55 55%,#d8d2cf)}

  /* section title */
  .title{font-size:40px;font-weight:600;color:var(--red);display:flex;align-items:center;gap:22px}
  .title::after{content:"";width:90px;height:2px;background:var(--red)}
  .title.center{justify-content:center}
  .title.center::before{content:"";width:90px;height:2px;background:var(--red)}

  .about h2{left:60px;top:768px}
  .about p{left:60px;top:840px;width:1080px;font-size:15px;line-height:1.6;color:var(--muted)}

  /* how it works */
  .how{left:0;top:940px;width:1200px;height:720px;background:linear-gradient(180deg,var(--blush) 0%,#fbf4f1 60%,var(--blush-deep) 100%)}
  .how .title{left:0;top:26px;width:1200px}
  .col-head{font-size:28px;font-weight:500;display:flex;align-items:center;gap:24px}
  .col-head::after{content:"";width:90px;height:2px;background:var(--ink)}
  .how .col-a{left:64px;top:128px}
  .how .col-b{left:620px;top:128px}
  .step{width:500px}
  .step h3{display:flex;align-items:center;gap:22px;font-size:22px;font-weight:500}
  .step h3 svg{width:24px;height:24px;flex:none}
  .step p{margin:22px 0 0 46px;font-size:14px;line-height:1.6;color:var(--muted);width:420px}

  /* why */
  .why-band{left:0;top:1700px;width:1200px;height:160px;background:var(--night)}
  .why-band h2{left:0;top:56px;width:1200px;text-align:center;color:#fff;font-size:40px;font-weight:600}
  .why{left:0;top:1860px;width:1200px;height:500px;background:linear-gradient(135deg,#f3e3dc,#fbf5f2 50%,#e9cfc6)}
  .card{width:280px;height:200px;background:var(--red);color:#fff;display:flex;align-items:center;justify-content:center;text-align:center;padding:0 28px;font-size:15px;font-weight:500;line-height:1.55;box-shadow:10px 10px 0 var(--red-dark),20px 20px 0 rgba(0,0,0,.18)}

  /* services */
  .services .title{left:0;top:2400px;width:1200px}
  .service{width:260px;display:flex;flex-direction:column;align-items:center;text-align:center}
  .service svg{width:80px;height:80px}
  .service h3{font-size:22px;font-weight:400;color:var(--red);line-height:1.2;height:58px;margin-top:10px;display:flex;align-items:center}
  .service .btn{margin-top:14px;height:40px}

  .strip{top:3088px;height:320px;width:240px}

  /* blog */
  .blog .title{left:0;top:3490px;width:1200px}
  .post{top:3580px;width:340px;text-align:center}
  .post .thumb{position:relative;height:180px;background:linear-gradient(135deg,#b9c9d6,#d7a99c 55%,#6c4b48)}
  .post .tag{position:absolute;left:14px;top:14px;background:var(--ink);color:#fff;font-size:11px;padding:4px 10px}
  .post time{display:block;margin-top:22px;font-size:12px;color:var(--muted)}
  .post h3{margin-top:8px;font-size:22px;font-weight:500;border-bottom:1px solid var(--line);padding-bottom:6px}
  .post .more{display:block;margin-top:8px;font-size:11px;color:var(--red);text-transform:uppercase}

  /* footer */
  .footer{left:0;top:3970px;width:1200px;height:462px;background:var(--foot)}
  .footer .brand{left:60px;top:40px;font-size:48px}
  .footer .blurb{left:60px;top:140px;width:280px;font-size:14px;line-height:1.6;color:var(--muted)}
  .socials{left:60px;top:236px;display:flex;gap:18px}
  .socials span{width:34px;height:34px;border:2px solid var(--red)}
  .foot-head{font-size:46px;font-weight:400;display:flex;align-items:center;gap:22px}
  .foot-head::after{content:"";width:80px;height:2px;background:var(--red)}
  .explore-head{left:420px;top:40px}
  .contact-head{left:790px;top:40px}
  .links{list-style:none;font-size:15px;line-height:2}
  .links li::before{content:"›";margin-right:8px;color:var(--red)}
  .places{list-style:none;left:800px;top:132px;font-size:15px;line-height:2.1;color:var(--red)}
  .places li{display:flex;align-items:center;gap:10px}
  .places svg{width:14px;height:18px}
  .rule{left:60px;top:384px;width:1080px;height:1px;background:var(--line)}
  .copy{left:0;top:408px;width:1200px;text-align:center;font-size:14px}
</style>
</head>
<body>

<header class="site-header abs">
  <ul class="nav">
    <li>Home<span class="dot"></span></li>
    <li>Our Services<span class="dot"></span></li>
    <li>Consultants</li>
  </ul>
  <div class="brand">Glowvra</div>
  <ul class="nav">
    <li class="nav-apply">Apply to be<br>Consultants<span class="dot"></span></li>
    <li>Glowvra Street<span class="dot"></span></li>
    <li>Contact Us</li>
  </ul>
</header>

<section class="hero abs">
  <h1 class="abs">Professional makeup</h1>
  <p class="abs">Integer dignissim, ante ac sagittis condimentum, magna est commodo urna, ut sagittis lorem est sit amet nibh. Class aptent taciti litora torquent.</p>
  <a class="btn abs" href="#">Read more</a>
  <div class="hero-photo one abs" role="img" aria-label="Fashion portrait of a model in a black military-style jacket and captain's cap"></div>
  <div class="hero-photo two abs" role="img" aria-label="Editorial portrait of a model with a floral headpiece and white top"></div>
</section>

<section class="about">
  <h2 class="title abs">About Us</h2>
  <p class="abs">Glowvra was founded with one key concept in mind: to provide a convenient connection for customers and professional makeup artists and estheticians who will enhance the look and feel that our customers want to achieve.</p>
</section>

<section class="how abs" role="region" aria-label="How Glowvra works">
  <h2 class="title center abs">How Glowvra Works</h2>

  <div class="col-a abs">
    <h3 class="col-head">For Clients</h3>
    <div class="step" style="margin-top:40px">
      <h3><svg viewBox="0 0 24 24"><rect x="10" y="2" width="4" height="13" fill="var(--red)"/><rect x="8" y="15" width="8" height="7" fill="var(--red)"/></svg>Explore</h3>
      <p>First, choose from our makeup or facial care services. If you don't see what you're looking for, create your custom look.</p>
    </div>
    <div class="step" style="margin-top:48px">
      <h3><svg viewBox="0 0 24 24" fill="none" stroke="var(--red)" stroke-width="2"><rect x="3" y="5" width="18" height="16"/><path d="M3 10h18M8 2v5M16 2v5"/></svg>Schedule</h3>
      <p>First, choose from our makeup or facial care services. If you don't see what you're looking for, create your custom look.</p>
    </div>
    <div class="step" style="margin-top:48px">
      <h3><svg viewBox="0 0 24 24" fill="none" stroke="var(--red)" stroke-width="2"><rect x="2" y="6" width="20" height="13"/><path d="M2 10h20"/></svg>Pay &amp; Get Glowvra</h3>
      <p>First, choose from our makeup or facial care services. If you don't see what you're looking for, create your custom look.</p>
    </div>
  </div>

  <div class="col-b abs">
    <h3 class="col-head">For Consultants</h3>
    <div class="step" style="margin-top:40px">
      <h3><svg viewBox="0 0 24 24" fill="var(--red)"><circle cx="9" cy="8" r="4"/><path d="M1 21c0-5 4-7 8-7s8 2 8 7z"/><circle cx="18" cy="9" r="3"/></svg>Build Your Client Base</h3>
      <p>First, choose from our makeup or facial care services. If you don't see what you're looking for, create your custom look.</p>
    </div>
    <div class="step" style="margin-top:48px">
      <h3><svg viewBox="0 0 24 24" fill="none" stroke="var(--red)" stroke-width="2"><circle cx="12" cy="12" r="10"/><path d="M12 6v6l4 3"/></svg>Manage Your Business</h3>
      <p>First, choose from our makeup or facial care services. If you don't see what you're looking for, create your custom look.</p>
    </div>
    <div class="step" style="margin-top:48px">
      <h3><svg viewBox="0 0 24 24" fill="none" stroke="var(--red)" stroke-width="2"><rect x="3" y="3" width="18" height="18"/><path d="M7 12l3 3 7-7"/></svg>Check Appointments and Go!</h3>
      <p>First, choose from our makeup or facial care services. If you don't see what you're looking for, create your custom look.</p>
    </div>
  </div>
</section>

<section class="why-band abs">
  <h2 class="abs">Why Glowvra?</h2>
</section>
<section class="why abs" role="img" aria-label="Soft backdrop of scattered makeup brushes and cosmetics">
  <div class="card abs" style="left:120px;top:40px">Access to service of the Washington Metropolitan area's most qualified and vetted professional makeup artists and estheticians</div>
  <div class="card abs" style="left:460px;top:40px">Convenience of having your makeup done in your home or at a location of your choosing</div>
  <div class="card abs" style="left:800px;top:40px">Sessions booked according to your schedule</div>
  <div class="card abs" style="left:120px;top:268px">Select the look that you want for any occasion</div>
  <div class="card abs" style="left:460px;top:268px">Preliminary test run included for your most important events</div>
  <div class="card abs" style="left:800px;top:268px">Access to Glowvra Street's blogs, tips, trends and makeup events</div>
</section>

<section class="services">
  <h2 class="title center abs">Services</h2>

  <div class="service abs" style="left:50px;top:2490px">
    <svg viewBox="0 0 80 80" fill="none" stroke="var(--ink)" stroke-width="3"><circle cx="40" cy="40" r="36"/><circle cx="32" cy="44" r="12"/><circle cx="48" cy="44" r="12"/><path d="M28 28l4-6 4 6"/></svg>
    <h3>Wedding</h3><a class="btn" href="#">Learn more</a>
  </div>
  <div class="service abs" style="left:330px;top:2490px">
    <svg viewBox="0 0 80 80" fill="none" stroke="var(--ink)" stroke-width="3"><circle cx="40" cy="40" r="36"/><rect x="24" y="36" width="8" height="22"/><rect x="36" y="28" width="8" height="30"/><rect x="48" y="40" width="8" height="18"/></svg>
    <h3>Full Makeup<br>Application</h3><a class="btn" href="#">Learn more</a>
  </div>
  <div class="service abs" style="left:610px;top:2490px">
    <svg viewBox="0 0 80 80" fill="none" stroke="var(--ink)" stroke-width="3"><circle cx="40" cy="40" r="36"/><rect x="20" y="26" width="40" height="28"/><circle cx="40" cy="40" r="6"/><path d="M36 54v8l4-3 4 3v-8"/></svg>
    <h3>Gift<br>Certificates</h3><a class="btn" href="#">Learn more</a>
  </div>
  <div class="service abs" style="left:890px;top:2490px">
    <svg viewBox="0 0 80 80" fill="none" stroke="var(--ink)" stroke-width="3"><circle cx="40" cy="40" r="36"/><path d="M22 26h16l-8 12zM30 38v16M24 54h12M42 26h16l-8 12zM50 38v16M44 54h12"/></svg>
    <h3>Group Party</h3><a class="btn" href="#">Learn more</a>
  </div>

  <div class="service abs" style="left:50px;top:2780px">
    <svg viewBox="0 0 80 80" fill="none" stroke="var(--ink)" stroke-width="3"><circle cx="40" cy="40" r="36"/><circle cx="40" cy="40" r="16"/><path d="M40 18v6M40 56v6M18 40h6M56 40h6"/></svg>
    <h3>Facial Care<br>Services</h3><a class="btn" href="#">Learn more</a>
  </div>
  <div class="service abs" style="left:330px;top:2780px">
    <svg viewBox="0 0 80 80" fill="none" stroke="var(--ink)" stroke-width="3"><circle cx="40" cy="40" r="36"/><rect x="22" y="26" width="36" height="24"/><path d="M36 32l10 6-10 6z" fill="var(--ink)"/><path d="M32 58h16"/></svg>
    <h3>Beauty<br>Tutorials</h3><a class="btn" href="#">Learn more</a>
  </div>
  <div class="service abs" style="left:610px;top:2780px">
    <svg viewBox="0 0 80 80" fill="none" stroke="var(--ink)" stroke-width="3"><circle cx="40" cy="40" r="36"/><path d="M26 54l20-28M46 26l8 4-6 8"/><circle cx="28" cy="28" r="5"/></svg>
    <h3>Men's<br>Grooming</h3><a class="btn" href="#">Learn more</a>
  </div>
  <div class="service abs" style="left:890px;top:2780px">
    <svg viewBox="0 0 80 80" fill="none" stroke="var(--ink)" stroke-width="3"><circle cx="40" cy="40" r="36"/><rect x="26" y="20" width="28" height="38"/><path d="M32 30h16M32 38h16M32 46h10"/></svg>
    <h3>Commercial<br>Contracts</h3><a class="btn" href="#">Learn more</a>
  </div>
</section>

<div class="strip abs" style="left:0;background:linear-gradient(135deg,#c4101f,#e8b7a8 60%,#7a1b1b)" role="img" aria-label="Close-up beauty portrait with bold red lipstick"></div>
<div class="strip abs" style="left:240px;background:linear-gradient(135deg,#f0e3d8,#c9a585 60%,#8b6b52)" role="img" aria-label="Beauty portrait of a blonde model with natural makeup"></div>
<div class="strip abs" style="left:480px;background:linear-gradient(135deg,#2b0d0f,#b0131e 50%,#e6c0b4)" role="img" aria-label="Red lipstick being applied to lips"></div>
<div class="strip abs" style="left:720px;background:linear-gradient(135deg,#d8d2cd,#9b7a66 55%,#3a2a25)" role="img" aria-label="Beauty portrait of a model with a sleek dark bob"></div>
<div class="strip abs" style="left:960px;background:linear-gradient(135deg,#efe6e1,#d0a892 55%,#5a3a30)" role="img" aria-label="Beauty portrait of a model touching her cheek"></div>

<section class="blog">
  <h2 class="title center abs">Blog</h2>
  <article class="post abs" style="left:60px">
    <div class="thumb" role="img" aria-label="Model with bright blue eye makeup"><span class="tag">MAKEUP</span></div>
    <time>30 Nov 2018</time><h3>BEAUTY TUTORIALS</h3><a class="more" href="#">Read more</a>
  </article>
  <article class="post abs" style="left:430px">
    <div class="thumb" role="img" aria-label="Model with bright blue eye makeup"><span class="tag">MAKEUP</span></div>
    <time>30 Nov 2018</time><h3>BEAUTY TUTORIALS</h3><a class="more" href="#">Read more</a>
  </article>
  <article class="post abs" style="left:800px">
    <div class="thumb" role="img" aria-label="Model with bright blue eye makeup"><span class="tag">MAKEUP</span></div>
    <time>30 Nov 2018</time><h3>BEAUTY TUTORIALS</h3><a class="more" href="#">Read more</a>
  </article>
</section>

<footer class="footer abs">
  <div class="brand abs">Glowvra</div>
  <p class="blurb abs">Etiam consequat sem ullamcorper, euismod metus sit amet, tristique justo. Vestibulum mattis.</p>
  <div class="socials abs"><span></span><span></span><span></span><span></span></div>

  <h3 class="foot-head explore-head abs">Explore</h3>
  <ul class="links abs" style="left:430px;top:132px"><li>Home</li><li>Consultants</li><li>Glowvra Street</li><li>Blog</li></ul>
  <ul class="links abs" style="left:590px;top:132px"><li>Gallery</li><li>Location</li><li>Our Services</li></ul>

  <h3 class="foot-head contact-head abs">Contact Us</h3>
  <ul class="places abs">
    <li><svg viewBox="0 0 14 18"><path d="M7 0a7 7 0 0 0-7 7c0 5 7 11 7 11s7-6 7-11a7 7 0 0 0-7-7z" fill="var(--red)"/><circle cx="7" cy="7" r="2.5" fill="#fff"/></svg>Virginia</li>
    <li><svg viewBox="0 0 14 18"><path d="M7 0a7 7 0 0 0-7 7c0 5 7 11 7 11s7-6 7-11a7 7 0 0 0-7-7z" fill="var(--red)"/><circle cx="7" cy="7" r="2.5" fill="#fff"/></svg>District of Columbia</li>
    <li><svg viewBox="0 0 14 18"><path d="M7 0a7 7 0 0 0-7 7c0 5 7 11 7 11s7-6 7-11a7 7 0 0 0-7-7z" fill="var(--red)"/><circle cx="7" cy="7" r="2.5" fill="#fff"/></svg>Maryland</li>
    <li><svg viewBox="0 0 14 18"><path d="M7 0a7 7 0 0 0-7 7c0 5 7 11 7 11s7-6 7-11a7 7 0 0 0-7-7z" fill="var(--red)"/><circle cx="7" cy="7" r="2.5" fill="#fff"/></svg>Florida</li>
  </ul>

  <div class="rule abs"></div>
  <p class="copy abs">© 2018 GLOWVRA</p>
</footer>

</body>
</html>
```